Fire and Building compliance company needs website

A professional website is needed for Kestow Alarm and Guard 2012 , company profile attached- we have a website but it is old and needs replacing (in fact we can not access it at present).

We are also looking at getting logo redesigned and will probably change to a flame type graphic with the letters KAG and then Fire and Building Compliance (bellow KAG).

It Company

• Ease of use
Page should fit inside typical screen size (not have to scroll down to see page).
Be made in Joomla 2.5

search words- Wanganui, fire alarm, building compliance, building warrant of fitness,BWOF, burglar alarm systems, LPG refilling,fire extinguishers, emergency lighting.

```html
<!DOCTYPE html>
<html lang="en">
<head>
<meta charset="utf-8">
<title>Kestow Alarm and Guard</title>
<link href="https://fonts.googleapis.com/css2?family=Roboto+Condensed:wght@300;400&family=Arimo:wght@400;700&display=swap" rel="stylesheet">
<style>
:root{
  --black:#000;
  --red:#d10000;
  --red-bright:#e00000;
  --white:#fff;
  --text:#333;
  --muted:#555;
  --light:#999;
  --nav-top:#3a3a3a;
  --nav-bottom:#0d0d0d;
  --divider:#555;
  --social:#3d6d9e;
}
*{margin:0;padding:0;box-sizing:border-box}
html,body{width:1200px;height:1047px;overflow:hidden;background:var(--white);font-family:Arimo,Arial,sans-serif;color:var(--text)}
.site-header{height:111px;background:var(--black);position:relative}
.brand{position:absolute;left:121px;top:22px;display:flex;align-items:center;gap:10px}
.brand-mark{width:48px;height:68px;background:var(--red)}
.brand-name{font-family:Arimo,Arial,sans-serif;font-weight:700;font-size:50px;color:var(--white);letter-spacing:1px;margin-top:12px}
.phone{position:absolute;right:118px;top:41px;display:flex;align-items:center;gap:12px}
.phone-icon{width:38px;height:38px;background:var(--red);border-radius:5px;display:flex;align-items:center;justify-content:center}
.phone-number{font-family:"Roboto Condensed",Arial,sans-serif;font-size:32px;color:var(--white)}
.main-nav{height:42px;background:linear-gradient(var(--nav-top),var(--nav-bottom));border-top:1px solid #666;border-bottom:1px solid #777}
.main-nav ul{list-style:none;display:flex;margin-left:120px;height:100%}
.main-nav li{font-size:16px;color:var(--white);padding:0 25px;line-height:40px;border-right:1px solid var(--divider)}
.main-nav li.active{background:var(--red);padding:0 21px}
.hero{background:var(--black);height:352px;position:relative}
.slide{position:absolute;left:120px;top:21px;width:960px;height:299px;border:3px solid var(--white);background:var(--black);overflow:hidden}
.slide-visual{position:absolute;left:0;top:0;right:0;bottom:0;background:linear-gradient(90deg,#000 0%,#000 40%,#5a1000 60%,#d05010 80%,#f08020 100%)}
.slide-copy{position:absolute;left:37px;top:54px;width:340px;color:var(--white)}
.slide-copy h1{font-family:"Roboto Condensed",Arial,sans-serif;font-weight:400;font-size:34px;margin-bottom:20px}
.slide-copy p{font-size:13.5px;line-height:17px}
.btn{display:inline-block;margin-top:48px;background:var(--red-bright);color:var(--white);font-size:17px;padding:6px 20px;border-radius:4px}
.dots{position:absolute;left:566px;top:330px;display:flex;gap:9px}
.dots span{width:10px;height:10px;border-radius:50%;background:var(--white)}
.dots span.on{background:var(--red);border:2px solid var(--white)}
.section-title{font-family:"Roboto Condensed",Arial,sans-serif;font-weight:400;font-size:29px;color:#111}
.section-title em{font-style:normal;color:var(--red)}
.specialise{position:absolute;left:120px;top:526px;width:960px}
.services{display:flex;justify-content:space-between;margin-top:11px}
.service{width:180px;text-align:center}
.service-image{height:99px;border:3px solid var(--red);background:linear-gradient(#eee,#ccc)}
.service-label{font-family:"Roboto Condensed",Arial,sans-serif;font-size:18px;color:#333;line-height:22px;margin-top:10px}
.welcome{position:absolute;left:121px;top:770px;width:530px}
.welcome p{font-size:13px;line-height:17px;color:var(--muted);margin-top:17px;letter-spacing:.3px}
.welcome .section-title+p{margin-top:16px}
.news{position:absolute;left:704px;top:770px;width:376px}
.news-item{display:flex;gap:17px;margin-top:20px}
.news-item svg{flex-shrink:0}
.news-date{color:var(--red);font-family:"Roboto Condensed",Arial,sans-serif;font-size:15px}
.news-title{font-size:14px;color:#444;margin:5px 0 3px;letter-spacing:.4px}
.news-body{font-size:13px;line-height:19px;color:var(--light)}
.news-more{text-align:right;font-size:12px;color:var(--red);margin-top:9px}
.site-footer{position:absolute;top:992px;left:0;width:1200px;height:55px;background:var(--black);color:var(--white);font-size:12.5px}
.footer-text{position:absolute;left:120px;top:8px;line-height:20px}
.social{position:absolute;right:120px;top:14px;display:flex;gap:8px}
.social span{width:24px;height:24px;border-radius:4px;background:var(--social)}
</style>
</head>
<body>
<header class="site-header">
  <div class="brand"><span class="brand-mark"></span><span class="brand-name">KAG</span></div>
  <div class="phone">
    <span class="phone-icon"><svg width="22" height="22" viewBox="0 0 24 24"><path d="M6.6 10.8a15 15 0 0 0 6.6 6.6l2.2-2.2c.3-.3.7-.4 1-.2 1.1.4 2.3.6 3.6.6.6 0 1 .4 1 1V20c0 .6-.4 1-1 1A17 17 0 0 1 3 4c0-.6.4-1 1-1h3.5c.6 0 1 .4 1 1 0 1.2.2 2.4.6 3.6.1.3 0 .7-.2 1z" fill="#000"/></svg></span>
    <span class="phone-number">(06)555 0147</span>
  </div>
</header>
<nav class="main-nav">
  <ul>
    <li class="active">Home</li><li>About</li><li>Services</li><li>Products</li><li>Media &amp; Events</li><li>Career</li><li>Contact</li>
  </ul>
</nav>
<section class="hero">
  <div class="slide">
    <div class="slide-visual" role="img" aria-label="Photo area: fire extinguisher in front of flames"></div>
    <div class="slide-copy">
      <h1>Fire Safety Training</h1>
      <p>As a Company we are able to offer full fire warden and evacuation training to assist with correct procedures in the event of an evacuation of your building.</p>
      <span class="btn">Read More</span>
    </div>
  </div>
  <div class="dots"><span></span><span class="on"></span><span></span><span></span></div>
</section>
<section class="specialise">
  <h2 class="section-title">We Specialise In</h2>
  <div class="services">
    <div class="service"><div class="service-image" role="img" aria-label="Sprinkler valve assembly" style="background:linear-gradient(#f2f2f2,#d8d8d8)"></div><div class="service-label">Automatic Sprinkler<br>Systems</div></div>
    <div class="service"><div class="service-image" role="img" aria-label="Red fire alarm strobe" style="background:linear-gradient(135deg,#e04030,#a01010)"></div><div class="service-label">Fire Alarms and<br>Emergency Lighting</div></div>
    <div class="service"><div class="service-image" role="img" aria-label="Motion sensor on a wall" style="background:linear-gradient(#e8e8e4,#bdbdb8)"></div><div class="service-label">Security Alarm<br>Systems</div></div>
    <div class="service"><div class="service-image" role="img" aria-label="Firefighter helmet" style="background:linear-gradient(135deg,#ddd,#e05020 55%,#c01010)"></div><div class="service-label">Fire Fighting &amp;<br>Compliance Specialists</div></div>
    <div class="service"><div class="service-image" role="img" aria-label="Modern office building with trees" style="background:linear-gradient(#6aa8e0,#c8d8e8 45%,#5a7a30)"></div><div class="service-label">Building Warrant of<br>Fitness Preparation</div></div>
  </div>
</section>
<section class="welcome">
  <h2 class="section-title">Welcome to <em>Kestow Alarm and Guard</em></h2>
  <p>Kestow Alarm &amp; Guard are members of the Fire Safety Guild (FSG) and are recognised as a leading authority in the design, installation and maintenance of fire alarms in the Wanganui area.&nbsp; Current Member of Building Circle.</p>
  <p>One of the most important areas of concern with fire alarms is the annual survey and without these comprehensive surveys, fire alarms can slip into a less than adequate state, all testing, maintenance and annual surveys are carried out as per NZS4512.</p>
</section>
<section class="news">
  <h2 class="section-title">Latest <em>News</em></h2>
  <div class="news-item">
    <svg width="50" height="50" viewBox="0 0 50 50"><rect x="2" y="6" width="46" height="42" rx="5" fill="#fff" stroke="#555" stroke-width="3"/><rect x="2" y="6" width="46" height="10" rx="4" fill="#555"/><rect x="12" y="1" width="4" height="10" rx="2" fill="#555"/><rect x="34" y="1" width="4" height="10" rx="2" fill="#555"/><text x="25" y="40" text-anchor="middle" font-family="Arimo,Arial,sans-serif" font-size="20" fill="#d10000">27</text></svg>
    <div>
      <div class="news-date">2 March 2013</div>
      <div class="news-title">Lorem ipsum dolor sit amet</div>
      <div class="news-body">Consectetur adipiscing elit. Duis vitae lectus sit met turpis molestie tempor. Vestibulum sollicitudin nibh sodales leo porta nec.</div>
    </div>
  </div>
  <div class="news-more">Read More &gt;</div>
</section>
<footer class="site-footer">
  <div class="footer-text">Copyright © 2012 Kestow Alarm and Guard.<br>Terms of Service &nbsp;|&nbsp; Privacy Policy</div>
  <div class="social"><span></span><span></span><span></span></div>
</footer>
</body>
</html>
```